Dellwick Underwriters LLC product offerings and how to contact for quotes

A marketing email to new and current clients explaining the products the MGA offers and it's exclusive programs. Looking for a modern/sleek design that catches the eye and doesn't become the traditional spam email. Needs to have hyper links to website.
You can use the current website for details of product offerings for insurance: www.dellwick-uw.example.
Target Market(s)
Long haul trucking
Industry/Entity Type
Trucking
Colors
0054AA
0677BA
7BADD7
CADEEF
E8F1F8
Requirements
Must have
- Color theme, informative, use of trucking art. Links to website.
Nice to have
- Catchy subject line; want to catch readers eye

```html
<!DOCTYPE html>
<html lang="en">
<head>
<meta charset="utf-8">
<title>Dellwick Underwriters – Products</title>
<link href="https://fonts.googleapis.com/css2?family=Poppins:wght@400;500;600;700&display=swap" rel="stylesheet">
<style>
:root{
  --blue:#0a4ea3;
  --blue-dark:#003f95;
  --blue-mid:#0677ba;
  --blue-light:#7badd7;
  --ice:#e8f1f8;
  --accent:#1a8ee0;
  --text:#333;
  --stage:#b5b5b5;
  --white:#fff;
}
*{margin:0;padding:0;box-sizing:border-box}
html,body{width:1200px;height:2851px;overflow:hidden;background:var(--stage);font-family:'Poppins',sans-serif}
.email{position:absolute;left:164px;top:160px;width:871px;height:2531px;background:var(--white);overflow:hidden}
.header{position:absolute;left:0;top:0;width:871px;height:103px}
.brand{position:absolute;left:65px;top:30px;display:flex;align-items:center;gap:8px;font-weight:700;font-size:22px;color:var(--blue);letter-spacing:.5px}
.brand .mark{width:14px;height:14px;border-radius:50%;background:var(--accent)}
.header-call{position:absolute;left:580px;top:28px;display:flex;align-items:center}
.header-call svg{width:32px;height:32px}
.header-call .divider{width:2px;height:42px;background:var(--accent);margin:0 18px 0 14px}
.header-call .label{font-size:16px;font-weight:500;color:var(--accent);line-height:20px}
.header-call .number{font-size:21px;font-weight:600;color:var(--blue);line-height:28px}
.hero{position:absolute;left:0;top:103px;width:871px;height:570px;background:linear-gradient(100deg,#e9eef3 0%,#c9d3de 30%,#8aa2c2 48%,var(--blue) 60%,var(--blue-dark) 100%)}
.hero-copy{position:absolute;left:469px;top:68px;color:var(--white);font-weight:600;text-transform:uppercase}
.hero-copy .sm{font-size:37px;line-height:48px;display:block}
.hero-copy .lg{font-size:60px;line-height:68px;font-weight:700;display:block}
.btn{position:absolute;display:flex;align-items:center;justify-content:center;width:204px;height:46px;border:2px solid var(--white);border-radius:24px;color:var(--white);font-size:14px;font-weight:600;text-decoration:none}
.hero .btn{left:476px;top:385px}
.hero-wave{position:absolute;left:0;top:560px;width:871px;height:120px}
.section-title{position:absolute;font-weight:600;color:var(--blue)}
.products-title{left:64px;top:680px;font-size:48px;line-height:62px}
.rule{position:absolute;height:3px;border-radius:2px;background:var(--accent)}
.product{position:absolute;width:262px;text-align:center}
.product .photo{width:228px;height:228px;border-radius:50%;margin:0 auto}
.product h3{margin-top:36px;font-size:19px;font-weight:600;color:var(--blue);line-height:24px}
.product .bar{width:78px;height:2px;background:var(--accent);margin:10px auto 0}
.product p{margin:20px auto 0;width:192px;font-size:11px;line-height:18.5px;color:var(--text);text-align:center}
.who{position:absolute;left:0;top:1771px;width:871px;height:570px;background:linear-gradient(160deg,#2a5fae 0%,var(--blue) 50%,#1b56a8 100%)}
.who h2{position:absolute;left:0;width:871px;top:58px;text-align:center;font-size:50px;font-weight:600;color:var(--white);line-height:64px}
.who .rule{left:364px;top:137px;width:142px}
.who p{position:absolute;left:66px;top:170px;width:740px;text-align:center;font-size:12.8px;line-height:28.8px;color:var(--white)}
.who .btn{left:334px;top:364px}
.who-wave{position:absolute;left:0;top:2240px;width:871px;height:110px}
.contact{position:absolute;top:2369px;display:flex;gap:15px}
.contact .icon{width:52px;height:52px;border-radius:50%;background:var(--blue);display:flex;align-items:center;justify-content:center;flex:none}
.contact .icon svg{width:26px;height:26px}
.contact h4{font-size:20px;font-weight:600;color:var(--blue);line-height:24px}
.contact .value{font-size:19.5px;color:#111;line-height:23px;margin-top:2px}
.footer{position:absolute;left:0;top:2456px;width:871px;height:75px;background:var(--blue);display:flex;align-items:center;justify-content:center}
.footer a{color:var(--white);font-size:30px;font-weight:500;text-decoration:none;text-transform:uppercase}
</style>
</head>
<body>
<div class="email">
  <header class="header">
    <div class="brand"><span class="mark"></span>Dellwick</div>
    <div class="header-call">
      <svg viewBox="0 0 24 24" fill="none" stroke="#0a4ea3" stroke-width="2" stroke-linecap="round" stroke-linejoin="round"><path d="M22 16.9v3a2 2 0 0 1-2.2 2 19.8 19.8 0 0 1-8.6-3.1 19.5 19.5 0 0 1-6-6A19.8 19.8 0 0 1 2.1 4.2 2 2 0 0 1 4.1 2h3a2 2 0 0 1 2 1.7c.1.9.4 1.8.7 2.7a2 2 0 0 1-.5 2.1L8 9.8a16 16 0 0 0 6 6l1.3-1.3a2 2 0 0 1 2.1-.4c.9.3 1.8.6 2.7.7a2 2 0 0 1 1.7 2z"/><path d="M15 2a7 7 0 0 1 7 7M15 6a3 3 0 0 1 3 3"/></svg>
      <span class="divider"></span>
      <div><div class="label">Call Us Now:</div><div class="number">(808) 555-0147</div></div>
    </div>
  </header>

  <section class="hero" role="img" aria-label="White semi truck parked at a loading dock, fading into blue">
    <div class="hero-copy">
      <span class="sm">Specializing in</span>
      <span class="sm">Tough-to-place</span>
      <span class="lg">Risks with</span>
      <span class="lg">Unmatched</span>
      <span class="sm">Customer Service</span>
    </div>
    <a class="btn" href="https://www.dellwick-uw.example">VIEW OUR SITE</a>
  </section>
  <svg class="hero-wave" viewBox="0 0 871 120" preserveAspectRatio="none"><path d="M0 65 C90 30 160 10 224 15 C420 25 560 115 711 108 C790 104 840 80 871 60 L871 120 L0 120 Z" fill="#fff"/></svg>

  <h2 class="section-title products-title">Our Products</h2>
  <div class="rule" style="left:61px;top:759px;width:142px"></div>

  <div class="product" style="left:43px;top:813px">
    <div class="photo" role="img" aria-label="White semi trucks at a warehouse dock" style="background:linear-gradient(160deg,#e4e8ee,#aeb8c4)"></div>
    <h3>Auto Liability</h3><div class="bar"></div>
    <p>Liability insurance is a part of the general insurance system of risk financing to protect the purchaser (the "insured") from the risks of liabilities imposed by lawsuits and similar claims.</p>
  </div>
  <div class="product" style="left:305px;top:813px">
    <div class="photo" role="img" aria-label="Two trucking workers checking paperwork" style="background:linear-gradient(160deg,#d9d4cc,#9aa07a)"></div>
    <h3>Non-Trucking Liability</h3><div class="bar"></div>
    <p>Non-Trucking Liability (NTL) provides coverage in case you cause an accident while you are using your vehicle for non-business or personal use other than transporting goods or merchandise.</p>
  </div>
  <div class="product" style="left:567px;top:813px">
    <div class="photo" role="img" aria-label="Tanker truck on a desert highway" style="background:linear-gradient(160deg,#8fa6c4,#6e6f74)"></div>
    <h3>Auto Physical Damage</h3><div class="bar"></div>
    <p>Physical Damage insurance is a type of insurance that covers damages to your truck and trailer. This type of coverage is typically offered as part of an auto insurance policy.</p>
  </div>

  <div class="product" style="left:43px;top:1273px">
    <div class="photo" role="img" aria-label="Trailer being loaded with cargo at a warehouse" style="background:linear-gradient(160deg,#6b5f55,#c9b8a0)"></div>
    <h3>Motor Truck Cargo</h3><div class="bar"></div>
    <p>Provides liability insurance for truckers who carry the cargo of others and is used in the event that the cargo is destroyed, damaged, stolen, or otherwise declared a loss while in the process</p>
  </div>
  <div class="product" style="left:305px;top:1273px">
    <div class="photo" role="img" aria-label="Semi trucks driving on a tree-lined road" style="background:linear-gradient(160deg,#8aaed0,#6f7c6a)"></div>
    <h3>General Liability</h3><div class="bar"></div>
    <p>General liability is often thought of when it comes to situations like a slip and fall. However, not many people realize that it would also cover any damages or bodily injury that your business</p>
  </div>
  <div class="product" style="left:567px;top:1273px">
    <div class="photo" role="img" aria-label="Row of parked semi trucks" style="background:linear-gradient(160deg,#b9cfe4,#8d8f96)"></div>
    <h3>Umbrella &amp; Excess Coverage</h3><div class="bar"></div>
    <p>Most Umbrella and Excess Liability policies are not written on standardized forms, so it is always important to read your policies to see what they actually cover.</p>
  </div>

  <section class="who" role="img" aria-label="Faint semi trucks on a highway under a blue overlay">
    <h2>Who We Are</h2>
    <div class="rule"></div>
    <p>Dellwick Underwriters LLC is a boutique Managing General Agent (MGA) specializing in commercial insurance for truckers. It was formed with one goal in mind: to help small independent trucking retailers with tough to place risks while giving them exceptional customer service experience. With knowledge and expertise in every aspect of a typical trucking operation, we want to be the preferred choice for our clients. We will never be too busy to respond back to your e-mails or phone calls. Here at Dellwick, we follow straight forward philosophy of very narrow producer base and working only with han...</p>
    <a class="btn" href="https://www.dellwick-uw.example">LEARN MORE</a>
  </section>
  <svg class="who-wave" viewBox="0 0 871 110" preserveAspectRatio="none"><path d="M0 46 C80 80 160 98 246 96 C430 92 560 10 711 7 C790 5 840 25 871 41 L871 110 L0 110 Z" fill="#fff"/></svg>

  <div class="contact" style="left:66px">
    <div class="icon"><svg viewBox="0 0 24 24" fill="none" stroke="#fff" stroke-width="2" stroke-linecap="round" stroke-linejoin="round"><path d="M22 16.9v3a2 2 0 0 1-2.2 2 19.8 19.8 0 0 1-8.6-3.1 19.5 19.5 0 0 1-6-6A19.8 19.8 0 0 1 2.1 4.2 2 2 0 0 1 4.1 2h3a2 2 0 0 1 2 1.7c.1.9.4 1.8.7 2.7a2 2 0 0 1-.5 2.1L8 9.8a16 16 0 0 0 6 6l1.3-1.3a2 2 0 0 1 2.1-.4c.9.3 1.8.6 2.7.7a2 2 0 0 1 1.7 2z"/></svg></div>
    <div><h4>CALL US</h4><div class="value">(808) 555-0147</div></div>
  </div>
  <div class="contact" style="left:466px">
    <div class="icon"><svg viewBox="0 0 24 24" fill="#fff"><path d="M12 2a7 7 0 0 0-7 7c0 5 7 13 7 13s7-8 7-13a7 7 0 0 0-7-7zm0 9.5A2.5 2.5 0 1 1 12 6.5a2.5 2.5 0 0 1 0 5z"/></svg></div>
    <div><h4>LOCATION</h4><div class="value">742 Harborline Ave Ste 210<br>Honolulu, HI 96801</div></div>
  </div>

  <footer class="footer"><a href="https://www.dellwick-uw.example">www.dellwick-uw.example</a></footer>
</div>
</body>
</html>
```